Need Letterhead Design & Matching Business Card

I have a logo that I love already. But the letterhead is less than appealing and boring. I'd like a design for my letterhead which I will match with business cards. Also, I'd like to have used fonts that are generally available, as my current letterhead uses a font named "SPACE" which nobody has unless they download it...so when a Word version is forwarded, it looks awful on the receiver's screed due to not having the font. That being said, modern is the look we like and are going for.

My business is "Hollister Brantley PC" - a law firm specializing in representing people who have suffered catastrophic injuries or death (plane, auto, train crashes etc.).

See attached letterhead, which has all of the pertinent information. My logo is also attached in various formats.

```html
<!DOCTYPE html>
<html lang="en">
<head>
<meta charset="utf-8">
<title>Hollister Brantley PC — Business Card</title>
<link rel="stylesheet" href="https://fonts.googleapis.com/css2?family=Open+Sans:wght@300;400;600&display=swap">
<style>
  :root {
    --backdrop: #d9d9d9;
    --ink: #231f20;
    --paper: #ffffff;
    --muted: #6d6d6d;
    --soft: #8a8a8a;
  }
  * { margin: 0; padding: 0; box-sizing: border-box; }
  html, body { width: 1200px; height: 800px; overflow: hidden; }
  body {
    background: var(--backdrop);
    font-family: "Open Sans", Arial, sans-serif;
    position: relative;
  }
  .card {
    position: absolute;
    left: 320px;
    width: 560px;
    height: 320px;
    box-shadow: 0 6px 18px rgba(0,0,0,0.18);
  }
  .card--front { top: 55px; background: var(--ink); }
  .card--back { top: 425px; background: var(--paper); }

  .brand {
    position: absolute;
    display: flex;
    align-items: center;
    gap: 16px;
  }
  .brand__square { flex: none; }
  .brand__name {
    font-weight: 300;
    text-transform: uppercase;
    letter-spacing: 0.14em;
    line-height: 1.1;
    white-space: nowrap;
  }
  .brand__suffix {
    font-size: 0.38em;
    letter-spacing: 0.2em;
    vertical-align: 0.9em;
    margin-left: 0.3em;
  }
  .card--front .brand { left: 80px; top: 110px; }
  .card--front .brand__square { width: 88px; height: 88px; background: var(--paper); }
  .card--front .brand__name { color: var(--paper); font-size: 36px; }

  .card--back .brand { right: 40px; top: 158px; }
  .card--back .brand__square { width: 46px; height: 46px; background: var(--ink); }
  .card--back .brand__name { color: var(--ink); font-size: 19px; }

  .card__tab {
    position: absolute;
    left: 0; top: 72px;
    width: 18px; height: 42px;
    background: var(--ink);
  }
  .contact { position: absolute; left: 90px; top: 36px; }
  .contact__name {
    font-weight: 600;
    font-size: 19px;
    letter-spacing: 0.03em;
    color: var(--ink);
    text-transform: uppercase;
    line-height: 1.3;
  }
  .contact__title { font-size: 18px; font-weight: 300; color: var(--muted); line-height: 1.3; }
  .contact__address { margin-top: 22px; font-size: 15px; line-height: 1.3; color: var(--soft); font-style: normal; }
  .contact__firm { color: var(--ink); }
  .contact__lines { margin-top: 14px; list-style: none; font-size: 15px; color: var(--soft); }
  .contact__lines li { display: flex; align-items: center; gap: 10px; line-height: 1.4; }
  .contact__lines svg { width: 14px; height: 14px; flex: none; }
</style>
</head>
<body>
  <section class="card card--front" aria-label="Card front">
    <div class="brand">
      <span class="brand__square"></span>
      <span class="brand__name">Hollister<br>Brantley<span class="brand__suffix">PC</span></span>
    </div>
  </section>

  <section class="card card--back" aria-label="Card back">
    <span class="card__tab"></span>
    <div class="contact">
      <p class="contact__name">Nolan R. Ashby</p>
      <p class="contact__title">Founder &amp; CEO</p>
      <address class="contact__address">
        <span class="contact__firm">Hollister Brantley PC</span><br>
        4820 Larkspur Ave.<br>
        Suite 600 Glendale,<br>
        CA 91203
      </address>
      <ul class="contact__lines">
        <li>
          <svg viewBox="0 0 16 16" aria-hidden="true"><path fill="#231f20" d="M3 2h3l1 3-2 1.2a8 8 0 0 0 4.8 4.8L11 9l3 1v3a1 1 0 0 1-1 1A11 11 0 0 1 2 3a1 1 0 0 1 1-1z"/></svg>
          555-214-7390
        </li>
        <li>
          <svg viewBox="0 0 16 16" aria-hidden="true"><rect x="1" y="3" width="14" height="10" fill="#231f20"/><path d="M1.5 3.5 8 9l6.5-5.5" fill="none" stroke="#fff" stroke-width="1.2"/></svg>
          info@hollisterbrantley.com
        </li>
        <li>
          <svg viewBox="0 0 16 16" aria-hidden="true"><circle cx="8" cy="8" r="7" fill="#231f20"/><path d="M1 8h14M8 1c-3 3.5-3 10.5 0 14M8 1c3 3.5 3 10.5 0 14" fill="none" stroke="#fff" stroke-width="0.9"/></svg>
          www.hollisterbrantley.com
        </li>
      </ul>
    </div>
    <div class="brand">
      <span class="brand__square"></span>
      <span class="brand__name">Hollister<br>Brantley<span class="brand__suffix">PC</span></span>
    </div>
  </section>
</body>
</html>
```